Vela Dorn Chinese Style Noodle Box Package

Kelunpan is an Asian food purveyor introducing a new line of Vela Dorn noodle products beginning with our 5-lbs box of dry Chinese style noodle directed at the Chinese population in the US. The Chinese markets are stacked with many low-price China imports...they are our only competitors. VD is the highest priced and best quality made in the tradition of the local renown Tam Brisk noodle (going-out-of-business). The noodle is versatile for any noodle dish: in soup, chow mein, saimin, lo mein, spaghetti, any noodle recipe. Vela Dorn is the brand. We want to standout from among the competitors, have a perceived high value and appeal to the Chinese noodle-eating population...most of whom came from China. Subsequent noodle products will be soba and udon.

```html
<!DOCTYPE html>
<html lang="en">
<head>
<meta charset="utf-8">
<title>Vela Dorn Noodle Range – Box Fronts</title>
<link rel="stylesheet" href="https://fonts.googleapis.com/css2?family=Barlow:wght@400;500;700&display=swap">
<style>
  :root {
    --page: #ffffff;
    --box-top: #240a0e;
    --box-mid: #5a0f24;
    --box-bottom: #d0145a;
    --band-chinese: #f0860e;
    --band-soba: #72c6bd;
    --band-rule: #3a1015;
    --title: #ffffff;
    --subtitle: #f29a2e;
    --copy: #e07a2a;
    --mark-bg: #1a0708;
    --mark-text: #ffffff;
    --note: #333333;
    --image-light: #f0d9a8;
    --image-dark: #8c5a3a;
  }
  * { box-sizing: border-box; margin: 0; padding: 0; }
  html, body { width: 1200px; height: 831px; overflow: hidden; background: var(--page); }
  body { position: relative; font-family: "Barlow", sans-serif; }

  .package {
    position: absolute;
    top: 45px;
    width: 376px;
    height: 733px;
    background: linear-gradient(180deg, var(--box-top) 0%, var(--box-top) 22%, var(--box-mid) 55%, var(--box-bottom) 100%);
    text-align: center;
    color: var(--title);
  }
  .package--chinese { left: 202px; }
  .package--soba { left: 627px; }

  .range-band {
    position: absolute;
    left: 0; right: 0;
    top: 28px;
    height: 50px;
    border-top: 2px solid var(--band-rule);
    border-bottom: 2px solid var(--band-rule);
  }
  .package--chinese .range-band { background: var(--band-chinese); }
  .package--soba .range-band { background: var(--band-soba); }

  .brand-mark {
    position: absolute;
    left: 136px;
    top: 22px;
    width: 104px;
    height: 80px;
    background: var(--mark-bg);
    border: 1px solid #6b2a2a;
    display: flex;
    align-items: center;
    justify-content: center;
  }
  .brand-mark__name {
    font-weight: 700;
    font-size: 15px;
    letter-spacing: 1.5px;
    text-transform: uppercase;
    color: var(--mark-text);
  }

  .product-name {
    position: absolute;
    left: 0; right: 0;
    top: 130px;
    font-weight: 700;
    font-size: 30px;
    line-height: 1;
    color: var(--title);
  }
  .product-type {
    position: absolute;
    left: 0; right: 0;
    top: 170px;
    font-weight: 400;
    font-size: 21px;
    line-height: 1;
    color: var(--subtitle);
  }
  .product-copy {
    position: absolute;
    left: 40px; right: 40px;
    top: 210px;
    font-size: 10px;
    line-height: 1.4;
    color: var(--copy);
  }

  .product-image {
    position: absolute;
    left: 60px;
    top: 282px;
    width: 262px;
    height: 400px;
    border-radius: 10px;
    background: radial-gradient(ellipse at 60% 40%, var(--image-light) 0%, rgba(200,150,100,0.55) 35%, rgba(140,90,58,0) 70%);
  }

  .package-footer {
    position: absolute;
    left: 22px; right: 22px;
    bottom: 22px;
    display: flex;
    justify-content: space-between;
    font-size: 11px;
    color: var(--title);
  }

  .design-note {
    position: absolute;
    left: 1027px;
    width: 150px;
    font-size: 9.5px;
    line-height: 1.45;
    color: var(--note);
  }
  .design-note--band { top: 80px; }
  .design-note--image { top: 422px; width: 110px; }
</style>
</head>
<body>

<section class="package package--chinese">
  <div class="range-band"></div>
  <div class="brand-mark"><span class="brand-mark__name">Vela Dorn</span></div>
  <h1 class="product-name">TamBrisk Noodle</h1>
  <h2 class="product-type">Chinese style noodle</h2>
  <p class="product-copy">A delicious, all purpose noodle perfect for ramen, spaghetti, noodle soup and any noodle dish.</p>
  <div class="product-image" role="img" aria-label="Photo of strands of Chinese style noodle lifted with black chopsticks"></div>
  <div class="package-footer"><span>Makes 4-6 servings</span><span>Net Wet. 13.5oz (383g)</span></div>
</section>

<section class="package package--soba">
  <div class="range-band"></div>
  <div class="brand-mark"><span class="brand-mark__name">Vela Dorn</span></div>
  <h1 class="product-name">Soba</h1>
  <h2 class="product-type">Japanese Buckwheat Noodle</h2>
  <p class="product-copy">A delicious, health noodle that may decrease cholesterol, lower blood pressure and reduce fat accumulation.</p>
  <div class="product-image" role="img" aria-label="Photo of strands of buckwheat soba noodle lifted with black chopsticks"></div>
  <div class="package-footer"><span>Makes 4-6 servings</span><span>Net Wet. 13.5oz (383g)</span></div>
</section>

<p class="design-note design-note--band">Segmentation colour for each within range</p>
<p class="design-note design-note--image">Final image will show actual noodle</p>

</body>
</html>
```